Flyer-Design für Energy-Drink
Zielgruppe
Es geht um einen neuen, gesunden Energy-Drink
Aufgabenstellung
Der Flyer sollte A5 entweder vorne und hinten bedruckt und ungefaltet sein
oder
A5 gefaltet auf A6 sein
Er soll junge Menschen ansprechen und hipp sein
Er soll erwachsene Menschen jeden Alters mit einem Gesundheitsbewusstsein ansprechen
Wichtig ist: kein Zuckerzusatz - 50% Fruchtanteil - ohne Chemie - absolut natürlich
wertvolle Vital und Inhaltsstoffe
einzigartiger, fruchtiger Geschmack, wenig Kohlensäure
gekühlt und geschüttelt trinken
Kick vor dem Sport oder einfach zwischendurch.
Neuer Antrieb
anregend, belebend
Dose ist zu 100% recycelbar

```html
<!DOCTYPE html>
<html lang="de">
<head>
<meta charset="utf-8">
<title>ZYNK – Flyer</title>
<link href="https://fonts.googleapis.com/css2?family=Montserrat:wght@700;800;900&display=swap" rel="stylesheet">
<style>
  :root {
    --page-bg: #8c8c8c;
    --dark: #2b2b2d;
    --dark-stripe: #3c3c3f;
    --red: #c41a1a;
    --red-deep: #8e0d0d;
    --yellow-glow: #f4c21c;
    --white: #f2f2f2;
    --ice-light: #cfe6f0;
    --ice-mid: #8fb4c4;
    --ice-dark: #3a4a52;
  }
  * { margin: 0; padding: 0; box-sizing: border-box; }
  html, body {
    width: 1200px; height: 1200px; overflow: hidden;
    background: var(--page-bg);
    font-family: "Montserrat", sans-serif;
  }
  .flyer {
    position: absolute; left: 210px; top: 50px;
    width: 780px; height: 1100px; overflow: hidden;
    background: var(--dark);
    box-shadow: 0 20px 50px rgba(0,0,0,.35);
  }
  .top-band {
    position: absolute; inset: 0 0 auto 0; height: 260px;
    background: repeating-linear-gradient(120deg, var(--dark) 0 22px, var(--dark-stripe) 22px 44px);
  }
  .red-stage {
    position: absolute; left: 0; right: 0; top: 200px; height: 720px;
    background:
      radial-gradient(circle at 16% 48%, var(--yellow-glow) 0 6%, rgba(255,120,20,.8) 14%, transparent 34%),
      radial-gradient(circle at 48% 58%, rgba(255,90,30,.6) 0 8%, transparent 30%),
      radial-gradient(ellipse at 60% 40%, var(--red) 0 45%, var(--red-deep) 100%);
  }
  .headline {
    position: absolute; z-index: 3;
    color: var(--white); font-weight: 900; line-height: .85; white-space: nowrap;
    text-shadow: 0 6px 12px rgba(0,0,0,.45);
  }
  .badge-new { position: absolute; z-index: 3; left: 28px; top: 100px; color: var(--red); font-weight: 900; font-size: 56px; }
  .headline-brand { left: 40px; top: 160px; font-size: 240px; letter-spacing: -6px; }
  .headline-your { right: 60px; top: 385px; font-size: 108px; }
  .headline-energy { right: 30px; top: 480px; font-size: 108px; letter-spacing: -2px; }
  .can {
    position: absolute; z-index: 1; left: 40px; top: 600px; width: 240px; height: 500px;
    border-radius: 40px 40px 0 0;
    background: linear-gradient(180deg, #b9b9b9 0 8%, #1c1c1c 13%, #7a1a1a 45%, #c0342c 60%, #1a1a1a 92%);
  }
  .benefits {
    position: absolute; z-index: 3; left: 330px; top: 620px; list-style: none;
    color: var(--white); font-weight: 700; font-size: 28px; line-height: 1.22;
    text-shadow: 0 3px 6px rgba(0,0,0,.5);
  }
  .benefits li::before { content: "• "; }
  .benefits .cont { padding-left: 18px; }
  .benefits .cont::before { content: ""; }
  .ice {
    position: absolute; z-index: 2; left: 0; right: 0; bottom: 0; height: 190px;
    background: linear-gradient(180deg, rgba(143,180,196,.35) 0%, var(--ice-mid) 30%, var(--ice-light) 60%, var(--ice-dark) 100%);
  }
</style>
</head>
<body>
  <main class="flyer">
    <div class="top-band"></div>
    <div class="red-stage" role="img" aria-label="Roter Hintergrund mit leuchtenden gelben und orangen Lichtpunkten"></div>
    <div class="badge-new">NEU!</div>
    <div class="headline headline-brand">ZYNK</div>
    <div class="headline headline-your">YOUR</div>
    <div class="headline headline-energy">ENERGY</div>
    <div class="can" role="img" aria-label="Foto einer schwarz-roten Getränkedose mit Wassertropfen und ZYNK-Aufschrift"></div>
    <ul class="benefits">
      <li>kein Zuckerzusatz</li>
      <li>keine Chemie</li>
      <li>wertvolle Vital- und</li>
      <li class="cont">Inhaltsstoffe</li>
      <li>50% Fruchtanteil</li>
      <li>anregend, belebend</li>
      <li>wenig Kohlensäure</li>
    </ul>
    <div class="ice" role="img" aria-label="Foto von klaren Eiswürfeln am unteren Rand"></div>
  </main>
</body>
</html>
```